Make it cool to work near where you are...

Calling all creatives - create the ultimate cool card for people who want to cut their commute.

Here at TilloPod we've got what can best be described as an Marlin pass for desks - and we want to brighten up the wallets of our most loyal users.

So, pitch us your ideas and you might see your design on cards being flashed across the country - and we've thrown in a bit of cash too.

Do see our brief card guidelines - with a couple of past examples thrown in.

Industry/Entity Type

Cash

```html
<!DOCTYPE html>
<html lang="en">
<head>
<meta charset="utf-8">
<title>TilloPod business card</title>
<link rel="stylesheet" href="https://fonts.googleapis.com/css2?family=Lato:wght@400;700;900&display=swap">
<style>
  :root {
    --page: #e9e6e1;
    --card-white: #ffffff;
    --charcoal: #3a3a3c;
    --charcoal-dark: #2b2b2d;
    --pink: #e3268e;
    --pink-soft: #ef7dbb;
    --ink: #2e2e30;
    --sky: #eef3f1;
    --hill: #9ccd5c;
    --text-light: #f2f2f2;
  }
  * { box-sizing: border-box; margin: 0; padding: 0; }
  html, body { width: 1200px; height: 900px; overflow: hidden; }
  body {
    background: var(--page);
    font-family: "Lato", Arial, sans-serif;
    position: relative;
  }
  .card {
    position: absolute;
    width: 520px;
    height: 300px;
    border-radius: 18px;
    overflow: hidden;
    background: var(--card-white);
    box-shadow: 0 10px 30px rgba(0,0,0,0.18);
  }
  .card--front { left: 60px; top: 130px; }
  .card--back { left: 620px; top: 470px; }

  /* Front */
  .front-band {
    position: absolute; left: 0; right: 0; bottom: 0; height: 130px;
    background: linear-gradient(180deg, var(--charcoal) 0%, var(--charcoal-dark) 100%);
  }
  .front-illustration {
    position: absolute; left: 0; top: 0; width: 520px; height: 230px;
  }
  .front-brand {
    position: absolute; right: 28px; top: 180px;
    font-weight: 900; font-size: 34px; color: var(--pink);
    letter-spacing: -0.5px;
  }
  .front-url {
    position: absolute; left: 30px; bottom: 26px;
    font-weight: 700; font-size: 17px; color: var(--text-light);
  }

  /* Back */
  .back-shape { position: absolute; inset: 0; }
  .back-brand {
    position: absolute; left: 34px; top: 76px;
    font-weight: 900; font-size: 34px; color: var(--pink);
    letter-spacing: -0.5px;
  }
  .person { position: absolute; left: 38px; top: 168px; }
  .person-name { font-weight: 700; font-size: 15px; color: var(--pink); }
  .person-role { font-size: 12px; color: var(--ink); }
  .contact {
    position: absolute; right: 26px; top: 96px;
    text-align: right; color: var(--text-light); font-size: 11.5px; line-height: 1.45;
  }
  .contact-address { margin-bottom: 12px; }
  .contact-line { display: flex; justify-content: flex-end; align-items: center; gap: 8px; }
  .contact-line svg { width: 12px; height: 12px; flex: none; }
</style>
</head>
<body>

<section class="card card--front">
  <div class="front-band"></div>
  <svg class="front-illustration" viewBox="0 0 520 230" role="img" aria-label="Illustration of a colourful city skyline with trees on rolling green hills">
    <defs>
      <linearGradient id="sceneGrad" x1="0" y1="0" x2="0" y2="1">
        <stop offset="0" stop-color="#eef3f1"/>
        <stop offset="0.55" stop-color="#e4eee0"/>
        <stop offset="1" stop-color="#9ccd5c"/>
      </linearGradient>
    </defs>
    <path d="M0 0 H520 V150 C470 140 430 150 400 170 C340 200 250 175 160 200 C100 215 50 215 0 230 Z" fill="url(#sceneGrad)"/>
  </svg>
  <div class="front-brand">TilloPod</div>
  <div class="front-url">www.tillopod.com</div>
</section>

<section class="card card--back">
  <svg class="back-shape" viewBox="0 0 520 300" aria-hidden="true">
    <defs>
      <linearGradient id="darkGrad" x1="0" y1="0" x2="1" y2="1">
        <stop offset="0" stop-color="#4a4a4c"/>
        <stop offset="1" stop-color="#2b2b2d"/>
      </linearGradient>
    </defs>
    <path d="M350 0 C300 20 285 90 265 150 C245 215 215 245 150 258 C100 268 50 270 0 272 V300 H520 V0 Z" fill="url(#darkGrad)"/>
    <path d="M345 -2 C295 20 280 90 260 150" fill="none" stroke="#ffffff" stroke-width="5"/>
    <path d="M470 0 C420 5 370 20 345 45" fill="none" stroke="var(--pink)" stroke-width="3"/>
    <path d="M258 158 C240 215 210 240 150 252" fill="none" stroke="#9a9a9c" stroke-width="6"/>
    <path d="M0 262 C70 260 150 258 215 238" fill="none" stroke="var(--pink)" stroke-width="14"/>
  </svg>

  <div class="back-brand">TilloPod</div>
  <div class="person">
    <p class="person-name">Sam Rowe</p>
    <p class="person-role">Managing Director</p>
  </div>

  <div class="contact">
    <p class="contact-address">WorkNook, 48-52 Calder Street<br>E2 7QA London, United Kingdom</p>
    <p class="contact-line">+44 20 7946 0318
      <svg viewBox="0 0 12 12" aria-hidden="true"><path d="M3 1 L5 3.5 L4 5 C4.8 6.6 5.6 7.4 7 8 L8.5 7 L11 9 L10 11 C5 11 1 7 1 2 Z" fill="#f2f2f2"/></svg>
    </p>
    <p class="contact-line">team@tillopod.com
      <svg viewBox="0 0 12 12" aria-hidden="true"><rect x="1" y="2.5" width="10" height="7" fill="none" stroke="#f2f2f2" stroke-width="1.2"/><path d="M1 2.5 L6 6.5 L11 2.5" fill="none" stroke="#f2f2f2" stroke-width="1.2"/></svg>
    </p>
    <p class="contact-line">www.tillopod.com
      <svg viewBox="0 0 12 12" aria-hidden="true"><circle cx="6" cy="6" r="5" fill="none" stroke="#f2f2f2" stroke-width="1.1"/><ellipse cx="6" cy="6" rx="2.2" ry="5" fill="none" stroke="#f2f2f2" stroke-width="1"/><path d="M1 6 H11" stroke="#f2f2f2" stroke-width="1"/></svg>
    </p>
  </div>
</section>

</body>
</html>
```